Dryer Vent Cleaning Postcard Design

We need a postcard design for Flue Wranglers, a company that specializes in dryer vent cleaning, repairs and upgrades. Dryer vents need periodic cleaning to avoid lint clogging, dryer malfunction, long dry times and even a house fire. This card will be sent to residential and businesses prospects to introduce them to our services and the importance of maintaining their dryer vents. Our website is @ fluewrangling.com and provides information about our services, photos of our work and our general color scheme (purple/orange). Final print size will be 5x7 horizontal.

Target Market(s)

homeowners and business owners (spas, salons, grooming, gyms, laundrymats, etc)

Requirements
Must have
• Reduce the risk of fire
shortened dry times
lower energy consumption
18000 dryer fires caused in the US per year
Nice to have
• Does your dryer take too long to dry?

```html
<!DOCTYPE html>
<html lang="en">
<head>
<meta charset="utf-8">
<title>Flue Wranglers – Dryer Vent Cleaning Postcard</title>
<link rel="stylesheet" href="https://fonts.googleapis.com/css2?family=League+Gothic&family=Source+Sans+3:wght@400;600;700&display=swap">
<style>
  :root {
    --ink: #1f1a38;
    --purple: #433a70;
    --bullet: #3d3374;
    --orange: #f2854e;
    --rust: #d2704c;
    --flame: #ef5a2f;
    --white: #ffffff;
    --paper: #ffffff;
  }
  * { margin: 0; padding: 0; box-sizing: border-box; }
  html, body { width: 1200px; height: 816px; overflow: hidden; background: var(--paper); }
  .canvas { position: relative; width: 1200px; height: 816px; overflow: hidden; font-family: "Source Sans 3", Arial, sans-serif; }
  .card { position: absolute; left: 0; top: 0; width: 1018px; height: 760px; }
  .card-bg { position: absolute; left: 0; top: 0; }

  .headline { font-family: "League Gothic", "Arial Narrow", sans-serif; font-weight: 400; color: var(--ink); }
  .headline span { position: absolute; line-height: 1; white-space: nowrap; }
  .headline .line-1 { left: 64px; top: 44px; font-size: 84px; letter-spacing: 1.5px; }
  .headline .line-2 { left: 48px; top: 146px; font-size: 66px; letter-spacing: 1px; }
  .headline .line-3 { left: 186px; top: 108px; font-size: 112px; letter-spacing: 1px; color: var(--white); }
  .headline .line-4 { left: 146px; top: 210px; font-size: 112px; letter-spacing: 2px; }

  .pitch { position: absolute; left: 500px; top: 36px; width: 500px; text-align: center; color: var(--white); font-size: 31px; line-height: 1.3; }
  .intro { position: absolute; left: 524px; top: 126px; width: 480px; color: var(--ink); font-size: 19px; line-height: 1.4; font-weight: 600; }

  .benefits { position: absolute; left: 554px; top: 208px; list-style: none; }
  .benefits li { display: flex; align-items: center; height: 47px; color: var(--bullet); font-size: 32px; }
  .benefits svg { width: 26px; height: 26px; margin-right: 11px; }

  .fact-tag { position: absolute; left: 591px; top: 413px; width: 253px; height: 49px; background: var(--ink); color: var(--white); font-size: 21px; padding: 10px 0 0 18px; }
  .fact { position: absolute; left: 594px; top: 468px; color: var(--ink); font-size: 21px; line-height: 1.08; font-weight: 600; }
  .flame { position: absolute; left: 550px; top: 462px; width: 34px; height: 50px; }

  .dryer-art { position: absolute; left: 816px; top: 366px; width: 164px; height: 194px; background: linear-gradient(180deg, #4a4650 0%, #d9d6d8 35%, #eeeceb 100%); }
  .guarantee { position: absolute; left: 660px; top: 558px; color: var(--white); font-size: 23px; transform: rotate(11deg); transform-origin: left top; white-space: nowrap; }

  .mascot-art { position: absolute; left: 108px; top: 312px; width: 300px; height: 246px; border-radius: 50% 50% 44% 44%; background: radial-gradient(ellipse at 50% 40%, #c9a892 0%, #7b9ccf 55%, #e8553a 100%); }
  .brand { position: absolute; left: 40px; top: 566px; width: 440px; display: flex; align-items: center; justify-content: center; gap: 12px; }
  .brand-dot { width: 30px; height: 30px; border-radius: 50%; background: var(--purple); }
  .brand-name { color: var(--purple); font-size: 44px; font-weight: 700; line-height: 1.1; }
  .web { position: absolute; left: 141px; top: 668px; color: var(--rust); font-size: 23px; font-weight: 700; }

  .call { position: absolute; right: 38px; top: 652px; color: var(--ink); font-size: 29px; font-weight: 600; white-space: nowrap; }
  .area { position: absolute; right: 33px; top: 693px; color: var(--purple); font-size: 14px; font-weight: 600; white-space: nowrap; }

  .swatches { position: absolute; left: 803px; top: 774px; display: flex; gap: 17px; }
  .swatch { width: 40px; height: 42px; }
  .swatch.ink { background: var(--ink); }
  .swatch.purple { background: var(--purple); }
  .swatch.rust { background: var(--rust); }
  .swatch.orange { background: var(--orange); }
</style>
</head>
<body>
<div class="canvas">
  <section class="card">
    <svg class="card-bg" width="1018" height="760" viewBox="0 0 1018 760" aria-hidden="true">
      <rect width="1018" height="760" fill="#ffffff"/>
      <path d="M0 0 H1018 V570 C930 622 830 632 720 602 C560 557 430 440 280 385 C170 348 80 392 0 424 Z" fill="var(--orange)"/>
      <path d="M0 424 C80 392 170 348 280 385 C430 440 560 557 720 602 C830 632 930 622 1018 570 V598 C930 652 820 662 710 632 C550 588 420 466 275 406 C170 368 80 412 0 447 Z" fill="var(--purple)"/>
    </svg>

    <h1 class="headline">
      <span class="line-1">Does your dryer</span>
      <span class="line-2">take</span>
      <span class="line-3">too long</span>
      <span class="line-4">to dry?</span>
    </h1>

    <p class="pitch">Damp clothes? Long dry times?<br>Get your vents cleaned!</p>
    <p class="intro">Flue Wranglers only uses the best equipment, materials, and craftsmanship to ensure every job is done correctly.</p>

    <ul class="benefits">
      <li><svg viewBox="0 0 24 24"><path d="M12 1l3 7 8 1-6 5 2 8-7-4-7 4 2-8-6-5 8-1z" fill="#fff"/></svg>Reduce the risk of fire</li>
      <li><svg viewBox="0 0 24 24"><path d="M12 1l3 7 8 1-6 5 2 8-7-4-7 4 2-8-6-5 8-1z" fill="#fff"/></svg>Shortened dry times</li>
      <li><svg viewBox="0 0 24 24"><path d="M12 1l3 7 8 1-6 5 2 8-7-4-7 4 2-8-6-5 8-1z" fill="#fff"/></svg>Lower energy consumption</li>
    </ul>

    <div class="fact-tag">You know that?</div>
    <svg class="flame" viewBox="0 0 34 50" aria-hidden="true">
      <path d="M17 0 C20 12 34 20 32 34 C30 45 22 50 17 50 C8 50 2 43 2 34 C2 26 8 22 10 14 C14 22 14 26 18 28 C22 20 16 10 17 0 Z" fill="var(--flame)"/>
    </svg>
    <p class="fact">18000 dryer fires caused<br>in the US per year!</p>

    <div class="dryer-art" role="img" aria-label="Illustration of a clothes dryer with dark smoke rising from its top"></div>

    <p class="guarantee">100% money back guarantee!</p>

    <div class="mascot-art" role="img" aria-label="Illustration of a vent technician holding a cleaning brush and hose in front of a blue oval badge"></div>
    <div class="brand">
      <span class="brand-dot"></span>
      <p class="brand-name">Flue Wranglers</p>
    </div>
    <p class="web">www.fluewrangling.com</p>

    <p class="call">Call Flue Wranglers NOW - 336-555-0147</p>
    <p class="area">Dryer vent cleaning in Greensboro NC, Summerfield, High Point, Winston Salem &amp; surrounding areas!</p>
  </section>

  <div class="swatches">
    <span class="swatch ink"></span>
    <span class="swatch purple"></span>
    <span class="swatch rust"></span>
    <span class="swatch orange"></span>
  </div>
</div>
</body>
</html>
```